Solo Law Practice Website Design

I am starting a solo law practice that will specialize in criminal defense and family law.

I have a rudimentary understanding of plain circle mark as used through the hostmerry web services. The winning design would be compatible with this system so that I can modify content on my own.

I have supplied the written content and the components that I am looking for at the domain name: dorianvaskelaw.example.

I would like to take that content and work it into a website that looks more professional and inviting. The two most important goals of the website are ease of navigation and rich content for search engine spiders (for example, integrating articles into pages rather than linking to a word document).

The winning design should be turnkey for me to upload immediately.
Updates

Reason: I will be traveling.

Target Market(s)

Individuals looking for legal services.

Industry/Entity Type

Defense

Requirements
Must have
• My picture should appear at least once in the site.

The design should allow a space for me to post blog or legal updates. Additionally, there should be functionality for me to add additional articles to the site.
Nice to have
• Appropriate pictures for a legal website to break-up text on pages.

Simple flash features that won't significantly slow loading times.

Widgets that drive traffic to a contact page or function.

```html
<!DOCTYPE html>
<html lang="en">
<head>
<meta charset="utf-8">
<title>Law Offices of Dorian Vaske PLLC</title>
<link rel="stylesheet" href="https://fonts.googleapis.com/css2?family=Arimo:wght@400;700&family=Cabin:wght@400&display=swap">
<style>
  :root {
    --admin-bg: #2f2f2f;
    --admin-text: #dddddd;
    --admin-divider: #444444;
    --accent-orange: #f5821f;
    --title-gray: #555555;
    --nav-border: #d6d6d6;
    --nav-text: #444444;
    --band: #fcf1dc;
    --band-line: #f0e2c6;
    --page-bg: #f6f6f6;
    --card-bg: #ffffff;
    --card-border: #dcdcdc;
    --heading: #555555;
    --body-text: #444444;
    --callout-bg: #e9eff7;
    --callout-border: #b9c8dc;
    --callout-text: #4a7ab8;
    --photo-tone: #5a1a08;
  }
  * { box-sizing: border-box; margin: 0; padding: 0; }
  html, body { width: 1200px; height: 582px; overflow: hidden; }
  body { background: var(--page-bg); font-family: "Arimo", Arial, sans-serif; color: var(--body-text); }
  .stage { position: relative; width: 1200px; height: 582px; overflow: hidden; background: var(--page-bg); }

  .admin-bar { position: absolute; left: 0; top: 0; width: 1200px; height: 25px; background: var(--admin-bg);
    display: flex; align-items: center; font-size: 12px; color: var(--admin-text); }
  .admin-item { height: 25px; display: flex; align-items: center; padding: 0 12px; border-right: 1px solid var(--admin-divider); gap: 6px; }
  .admin-mark { width: 17px; height: 17px; border-radius: 50%; border: 2px solid #aaaaaa; }
  .admin-right { margin-left: auto; display: flex; height: 25px; }
  .admin-right .admin-item { border-right: none; border-left: 1px solid var(--admin-divider); }
  .avatar { width: 16px; height: 16px; background: #b23a2a; }

  .site-header { position: absolute; left: 0; top: 25px; width: 1200px; height: 145px; background: #ffffff; }
  .top-rule { position: absolute; left: 171px; top: 0; width: 844px; height: 4px; background: var(--accent-orange); }
  .site-title { position: absolute; left: 189px; top: 32px; font-family: "Cabin", sans-serif; font-size: 37px; color: var(--title-gray); font-weight: 400; letter-spacing: -0.5px; }

  .main-nav { position: absolute; left: 171px; top: 129px; height: 41px; display: flex; border: 1px solid var(--nav-border); border-bottom: none; background: #ffffff; width: 844px; }
  .main-nav a { display: flex; align-items: center; justify-content: center; border-right: 1px solid var(--nav-border);
    font-size: 10.5px; font-weight: 700; color: var(--nav-text); text-decoration: none; height: 100%; }

  .accent-band { position: absolute; left: 0; top: 170px; width: 1200px; height: 19px; background: var(--band);
    border-top: 1px solid var(--band-line); border-bottom: 1px solid var(--band-line); }

  .content-card { position: absolute; left: 180px; top: 208px; width: 826px; height: 400px; background: var(--card-bg); border: 1px solid var(--card-border); }
  .page-heading { position: absolute; left: 22px; top: 34px; width: 560px; font-size: 26px; line-height: 30px; font-weight: 700; color: var(--heading); }
  .intro { position: absolute; left: 22px; top: 122px; width: 560px; font-size: 12.3px; line-height: 21px; }
  .intro strong { font-weight: 700; }

  .portrait-frame { position: absolute; left: 632px; top: 26px; width: 174px; height: 168px; border: 1px solid var(--card-border); background: #ffffff; }
  .portrait { position: absolute; left: 3px; top: 3px; width: 166px; height: 134px; background: linear-gradient(135deg, #6b2410, var(--photo-tone) 60%, #3a0f04); }
  .portrait-caption { position: absolute; left: 0; top: 143px; width: 100%; text-align: center; font-size: 9.5px; color: #555555; }

  .callout { position: absolute; left: 22px; top: 240px; width: 780px; height: 69px; background: var(--callout-bg); border: 1px solid var(--callout-border); border-radius: 3px;
    padding: 15px 20px 0 33px; font-size: 12.3px; line-height: 21px; color: var(--callout-text); }
  .callout-icon { position: absolute; left: 12px; top: 16px; }

  .feature-columns { position: absolute; left: 22px; top: 324px; display: flex; gap: 33px; }
  .feature { width: 237px; font-size: 12.3px; line-height: 21px; }
</style>
</head>
<body>
<div class="stage">
  <div class="admin-bar">
    <div class="admin-item"><span class="admin-mark"></span></div>
    <div class="admin-item">Law Offices of Dorian Vaske PLLC</div>
    <div class="admin-item">
      <svg width="14" height="12" viewBox="0 0 14 12"><path d="M1 1h12v7H6l-3 3V8H1z" fill="#aaaaaa"/></svg>
    </div>
    <div class="admin-item"><strong style="font-size:14px">+</strong> New</div>
    <div class="admin-item">Edit Page</div>
    <div class="admin-right">
      <div class="admin-item">Howdy, owen <span class="avatar"></span></div>
      <div class="admin-item">
        <svg width="12" height="12" viewBox="0 0 12 12"><circle cx="7" cy="5" r="3.5" stroke="#aaaaaa" stroke-width="1.6" fill="none"/><path d="M4.5 7.5L1 11" stroke="#aaaaaa" stroke-width="1.8"/></svg>
      </div>
    </div>
  </div>

  <header class="site-header">
    <div class="top-rule"></div>
    <h1 class="site-title">Law Offices of Dorian Vaske PLLC</h1>
    <nav class="main-nav" style="top:104px">
      <a href="#" style="width:40px"><svg width="11" height="10" viewBox="0 0 11 10"><path d="M5.5 0L11 5H9.5v5H6.5V7h-2v3H1.5V5H0z" fill="#cccccc"/></svg></a>
      <a href="#" style="width:79px">Contact Me</a>
      <a href="#" style="width:88px">Criminal Law</a>
      <a href="#" style="width:77px">Family Law</a>
      <a href="#" style="width:83px">Will Drafting</a>
      <a href="#" style="width:101px">Attorney Profile</a>
      <a href="#" style="width:47px">Fees</a>
      <a href="#" style="width:94px">Legal Updates</a>
      <a href="#" style="width:112px">Online Resources</a>
      <a href="#" style="width:62px">Articles</a>
    </nav>
  </header>

  <div class="accent-band"></div>

  <main class="content-card">
    <h2 class="page-heading">Specializing in Criminal Defense and Family Law</h2>
    <p class="intro"><strong>Delivering legal services in the greater Twin Cities area.</strong><br>
      <strong>About Me.</strong>&nbsp; My practice is focused on accomplishing your goals through results-oriented work at a discount price.&nbsp; For your convenience, I handle legal matters throughout the Twin Cities, including Hennepin, Ramsey, Anoka, and Washington counties.&nbsp; I understand that legal issues can appear complicated, and that is why I take a hands-on approach to guiding you through your legal needs.</p>

    <figure class="portrait-frame">
      <div class="portrait" role="img" aria-label="Portrait photograph of attorney Dorian Vaske in a dark suit"></div>
      <figcaption class="portrait-caption">Dorian Vaske, Attorney</figcaption>
    </figure>

    <aside class="callout">
      <svg class="callout-icon" width="13" height="13" viewBox="0 0 13 13"><circle cx="6.5" cy="6.5" r="6" fill="#5d86bd"/><text x="6.5" y="10" text-anchor="middle" font-size="9" font-weight="700" fill="#ffffff" font-family="Arimo, sans-serif">?</text></svg>
      <strong>Contact me.</strong>&nbsp; To discuss how the Law Offices of Dorian Vaske can help you, call us at (612) 555-0148 to arrange for you free consultation.
    </aside>

    <section class="feature-columns">
      <p class="feature"><strong>Personal Attention.</strong>&nbsp; I control the size of my practice so that I am able to devote 100% of my effort to each case.&nbsp; I have no</p>
      <p class="feature"><strong>General Practice.</strong>&nbsp; I am available to provide your defense if you are accused of a felony or misdemeanor.&nbsp; Additionally, I</p>
      <p class="feature"><strong>In our first consultation,</strong> I will take time to listen to your individual situation.&nbsp; I will explain the legal issues, and the risks</p>
    </section>
  </main>
</div>
</body>
</html>
```